Lindenfield Advocacy Learning Forums
Icon Set
We wish to design an icon set to be used in printed brochures as well as our website and other marketing materials.
Law
Professional - Lawyers. LALF provides legal training and education seminar for lawyers.
LALF organises and presents regular legal professional seminars throughout Australia. Our marketing is heavily based on direct mail. When we schedule our seminars we design and print brochures and send them to all lawyers that are close to the location of the seminars.
All lawyers in Australia are required to attend a specified number of hours of continuing education seminars each year. For every hour of attendance, they can gain 1 point and they usually need to accumulate 10-20 points per year.
In most cases there are also compulsory areas that must be covered. Each State has different requirements, but there are four main compulsory areas:
1. Legal Ethics
2. Practice Management or Business Skills
3. Professional Skills
4. Substantive Law
There is also an additional subject area which is used in one location (Sydney) – this is for OH & S, Employment Law, Equal Opportunity and Discrimination Law.
We always designate how many points (or hours) a lawyer will get by attending one of our seminars and in which compulsory area they will get the points.
What we need is an icon for each of the four main areas. Each icon should ideally be recognizable with the particular compulsory area and be a different colour. We would also like an icon for the additional subject area in Sydney, but this is not essential.
Also, it would be ideal if the points and/or description of the compulsory area could be incorporated within the icon graphic. However, if this is not possible, then this can be done as text under the icon or to the side.
The icon does not need to be any particular size – it could be square, round, rectangle or anything else. But, please remember the context we will be using it in. The main use will be in the marketing brochures. But we would also like to use it on our website and other media as required.
I will also need to be able to edit each icon as the descriptions of the compulsory subjects differ slightly between the States. I will also need to be able to change the number of points. Ideally, I should be able to edit the icons using Adobe Illustrator.
I will upload several examples of our marketing brochures which show how we currently designate points/compulsory areas for each seminar. The icons we use at the moment are a set of stock-icons I purchased on the web. However, these icons were never ideal and we would like something that is specifically designed for our purposes.
Also, if you look at the back panel of each brochure (panel 5 on the first page), there is a description of what each icon represents and more information on the compulsory subjects. This information is different for each State.
I will also upload some examples of icons used by some of our competitors. Please note that none of these examples actually specify the number of points within the graphic. This is not ideal. I think a clear number should be included in the graphic. For example, if the seminar has 3 points – then a clear “3” should stand out in the icon.
Finally, please also note that I wish to redesign the template we use for our marketing brochures. I will create a separate project for this, but you may wish to consider submitting a design for this as well. Please see this project for the specific details.
Example of Sydney Brochure
Example of Melbourne Brochure
Example of Brisbane Brochure
Example of Perth Brochure

```html
<!DOCTYPE html>
<html lang="en">
<head>
<meta charset="UTF-8">
<title>Lindenfield Advocacy Learning Forums – Compulsory Area Icons</title>
<link rel="stylesheet" href="https://fonts.googleapis.com/css2?family=Arimo:wght@700&display=swap">
<style>
  :root {
    --canvas-bg: #ffffff;
    --rim-outer: #c9c9c9;
    --rim-inner: #ffffff;
    --label-ink: #ffffff;
    --ethics-light: #ee5fcb;
    --ethics-dark: #b3127f;
    --skills-light: #3f7fe6;
    --skills-dark: #163f9e;
    --practice-light: #e03a3f;
    --practice-dark: #9c0f18;
    --law-light: #74c743;
    --law-dark: #3a8f1c;
  }
  html, body {
    margin: 0;
    padding: 0;
    width: 1200px;
    height: 600px;
    overflow: hidden;
    background: var(--canvas-bg);
  }
  .icon-set { display: block; width: 1200px; height: 600px; }
  .badge-label {
    font-family: "Arimo", Arial, sans-serif;
    font-weight: 700;
    font-size: 37px;
    fill: var(--label-ink);
    text-anchor: middle;
  }
  .label-shadow { fill: rgba(0,0,0,0.28); }
  .pill-rim { fill: var(--rim-inner); stroke: var(--rim-outer); stroke-width: 3; }
  .disc-rim-outer { fill: var(--rim-outer); }
  .disc-rim-inner { fill: var(--rim-inner); }
  .gloss { fill: #ffffff; opacity: 0.28; }
  .glyph { fill: #ffffff; }
  .glyph-line { fill: none; stroke: #ffffff; stroke-width: 4; stroke-linecap: round; }
</style>
</head>
<body>
<svg class="icon-set" viewBox="0 0 1200 600" xmlns="http://www.w3.org/2000/svg" role="img" aria-label="Compulsory area icons: Legal Ethics, Professional Skills, Pratice Management, Substantive Law">
  <defs>
    <linearGradient id="fill-ethics" x1="0" y1="0" x2="0" y2="1">
      <stop offset="0" stop-color="var(--ethics-light)"/><stop offset="1" stop-color="var(--ethics-dark)"/>
    </linearGradient>
    <linearGradient id="fill-skills" x1="0" y1="0" x2="0" y2="1">
      <stop offset="0" stop-color="var(--skills-light)"/><stop offset="1" stop-color="var(--skills-dark)"/>
    </linearGradient>
    <linearGradient id="fill-practice" x1="0" y1="0" x2="0" y2="1">
      <stop offset="0" stop-color="var(--practice-light)"/><stop offset="1" stop-color="var(--practice-dark)"/>
    </linearGradient>
    <linearGradient id="fill-law" x1="0" y1="0" x2="0" y2="1">
      <stop offset="0" stop-color="var(--law-light)"/><stop offset="1" stop-color="var(--law-dark)"/>
    </linearGradient>
  </defs>

  <!-- Legal Ethics -->
  <g class="badge badge-ethics" transform="translate(168 197)">
    <rect class="pill-rim" x="0" y="-58" width="426" height="116" rx="24"/>
    <rect x="6" y="-52" width="414" height="104" rx="19" fill="url(#fill-ethics)"/>
    <path class="gloss" d="M6 -33 Q6 -52 25 -52 H401 Q420 -52 420 -33 V-4 H6 Z"/>
    <text class="badge-label label-shadow" x="252" y="16">Legal Ethics</text>
    <text class="badge-label" x="250" y="13">Legal Ethics</text>
    <circle class="disc-rim-outer" r="70"/>
    <circle class="disc-rim-inner" r="65"/>
    <circle r="58" fill="url(#fill-ethics)"/>
    <path class="gloss" d="M-56 -6 A56 56 0 0 1 56 -6 Z"/>
    <g class="glyph">
      <polygon points="0,-38 -36,-18 36,-18"/>
      <rect x="-36" y="-15" width="72" height="6"/>
      <rect x="-30" y="-7" width="9" height="34"/>
      <rect x="-14" y="-7" width="9" height="34"/>
      <rect x="5" y="-7" width="9" height="34"/>
      <rect x="21" y="-7" width="9" height="34"/>
      <rect x="-38" y="29" width="76" height="7"/>
    </g>
  </g>

  <!-- Professional Skills -->
  <g class="badge badge-skills" transform="translate(691 197)">
    <rect class="pill-rim" x="0" y="-58" width="426" height="116" rx="24"/>
    <rect x="6" y="-52" width="414" height="104" rx="19" fill="url(#fill-skills)"/>
    <path class="gloss" d="M6 -33 Q6 -52 25 -52 H401 Q420 -52 420 -33 V-4 H6 Z"/>
    <text class="badge-label label-shadow" x="252" y="-5">Professional</text>
    <text class="badge-label" x="250" y="-8">Professional</text>
    <text class="badge-label label-shadow" x="252" y="36">Skills</text>
    <text class="badge-label" x="250" y="33">Skills</text>
    <circle class="disc-rim-outer" r="70"/>
    <circle class="disc-rim-inner" r="65"/>
    <circle r="58" fill="url(#fill-skills)"/>
    <path class="gloss" d="M-56 -6 A56 56 0 0 1 56 -6 Z"/>
    <g class="glyph">
      <circle cx="0" cy="-34" r="4"/>
      <rect x="-2.5" y="-32" width="5" height="62"/>
      <rect x="-36" y="-28" width="72" height="4"/>
      <rect x="-16" y="30" width="32" height="6" rx="2"/>
      <path d="M-46 2 A12 8 0 0 0 -14 2 Z"/>
      <path d="M14 2 A12 8 0 0 0 46 2 Z"/>
    </g>
    <path class="glyph-line" style="stroke-width:2" d="M-34 -25 L-45 2 M-34 -25 L-15 2 M34 -25 L15 2 M34 -25 L45 2"/>
  </g>

  <!-- Pratice Management -->
  <g class="badge badge-practice" transform="translate(168 389)">
    <rect class="pill-rim" x="0" y="-58" width="426" height="116" rx="24"/>
    <rect x="6" y="-52" width="414" height="104" rx="19" fill="url(#fill-practice)"/>
    <path class="gloss" d="M6 -33 Q6 -52 25 -52 H401 Q420 -52 420 -33 V-4 H6 Z"/>
    <text class="badge-label label-shadow" x="252" y="-5">Pratice</text>
    <text class="badge-label" x="250" y="-8">Pratice</text>
    <text class="badge-label label-shadow" x="252" y="36">Management</text>
    <text class="badge-label" x="250" y="33">Management</text>
    <circle class="disc-rim-outer" r="70"/>
    <circle class="disc-rim-inner" r="65"/>
    <circle r="58" fill="url(#fill-practice)"/>
    <path class="gloss" d="M-56 -6 A56 56 0 0 1 56 -6 Z"/>
    <g class="glyph" transform="rotate(-40)">
      <rect x="-10" y="-40" width="20" height="44" rx="4"/>
      <rect x="-12" y="-36" width="24" height="5" rx="2"/>
      <rect x="-12" y="-5" width="24" height="5" rx="2"/>
      <rect x="-4" y="-20" width="46" height="8" rx="3"/>
    </g>
    <rect class="glyph" x="-38" y="26" width="40" height="9" rx="2"/>
  </g>

  <!-- Substantive Law -->
  <g class="badge badge-law" transform="translate(691 389)">
    <rect class="pill-rim" x="0" y="-58" width="426" height="116" rx="24"/>
    <rect x="6" y="-52" width="414" height="104" rx="19" fill="url(#fill-law)"/>
    <path class="gloss" d="M6 -33 Q6 -52 25 -52 H401 Q420 -52 420 -33 V-4 H6 Z"/>
    <text class="badge-label label-shadow" x="252" y="-5">Substantive</text>
    <text class="badge-label" x="250" y="-8">Substantive</text>
    <text class="badge-label label-shadow" x="252" y="36">Law</text>
    <text class="badge-label" x="250" y="33">Law</text>
    <circle class="disc-rim-outer" r="70"/>
    <circle class="disc-rim-inner" r="65"/>
    <circle r="58" fill="url(#fill-law)"/>
    <path class="gloss" d="M-56 -6 A56 56 0 0 1 56 -6 Z"/>
    <g class="glyph" transform="rotate(45)">
      <path d="M0 -8 C-12 -2 -14 14 -8 22 L0 46 L8 22 C14 14 12 -2 0 -8 Z"/>
      <rect x="-9" y="-20" width="18" height="10" rx="2"/>
    </g>
    <path class="glyph-line" d="M-30 34 Q-10 40 6 30 Q20 22 34 24"/>
  </g>
</svg>
</body>
</html>
```